RAY DUNMORE INSTITUTE

I need one trifold brochure that can describe our company and what we do. Our site is www.raydunmoreinstitute-example.com Right now there is just one program we offer. A 52 week leadership development program called "Charting A Bolder Morning". The way our program works is you enroll for 97.95 and then you receive an email each week with a pdf file of a lesson and a video from one of our experts discussing the lesson. Its like Gary Feldwick meets zolo forums meets chatterbay. We have a leader in Ray Dunmore, video segmets from our experts in a community of thousands.
Leadership

```html
<!DOCTYPE html>
<html lang="en">
<head>
<meta charset="utf-8">
<title>Ray Dunmore Institute – Trifold Brochure</title>
<link rel="stylesheet" href="https://fonts.googleapis.com/css2?family=Ubuntu:wght@400;500;700&display=swap">
<style>
  :root {
    --brand-blue: #3b7cc9;
    --brand-blue-dark: #2e66ad;
    --navy: #17304d;
    --paper: #ffffff;
    --body-grey: #6a6a6a;
    --ink: #1d1d1d;
    --stage-top: #ffffff;
    --stage-bottom: #d9d9d9;
  }
  * { box-sizing: border-box; margin: 0; padding: 0; }
  html, body { width: 1200px; height: 900px; overflow: hidden; }
  body {
    background: linear-gradient(180deg, var(--stage-top) 0%, #efefef 55%, var(--stage-bottom) 100%);
    font-family: "Ubuntu", sans-serif;
  }
  .brochure {
    position: absolute;
    left: 150px; top: 100px;
    width: 900px; height: 700px;
    display: flex;
    box-shadow: 0 10px 30px rgba(0,0,0,0.18);
  }
  .panel {
    position: relative;
    width: 300px; height: 700px;
    background: var(--paper);
    overflow: hidden;
  }
  .panel + .panel { border-left: 1px solid #e6e6e6; }

  /* Cover */
  .cover { background: var(--navy); }
  .cover-band {
    position: absolute; left: 0; top: 42px;
    width: 300px; height: 82px;
    background: var(--paper);
    display: flex; align-items: center; padding-left: 22px;
  }
  .cover-art { position: absolute; left: 0; top: 124px; }

  .wordmark { display: flex; align-items: center; gap: 9px; }
  .wordmark-square { width: 20px; height: 20px; background: var(--navy); flex: none; }
  .wordmark-name {
    font-weight: 400; font-size: 21px; color: var(--ink); letter-spacing: -0.2px; white-space: nowrap;
  }

  /* Inner panels */
  .panel-header {
    position: absolute; top: 30px; left: 20px;
    width: 178px; height: 40px;
    background: linear-gradient(90deg, var(--brand-blue-dark), var(--brand-blue));
    color: #fff; font-weight: 700; font-size: 19px;
    display: flex; align-items: center; padding-left: 12px;
    white-space: nowrap;
  }
  .panel-body {
    position: absolute; top: 98px; left: 20px; right: 20px;
    color: var(--body-grey);
    font-size: 9.6px; line-height: 1.42;
    text-align: justify;
  }
  .panel-body p + p { margin-top: 11px; }

  .feature-tiles {
    position: absolute; left: 20px; right: 20px; top: 400px;
    display: flex; flex-direction: column; gap: 14px; align-items: flex-end;
  }
  .feature-tile {
    width: 120px; height: 110px;
    display: flex; align-items: center; justify-content: center;
  }
  .feature-tile--light { background: var(--brand-blue); }
  .feature-tile--dark { background: var(--brand-blue-dark); }

  .circle-panel .wordmark { position: absolute; right: 20px; bottom: 40px; }
</style>
</head>
<body>
  <main class="brochure">
    <!-- Front cover -->
    <section class="panel cover">
      <div class="cover-band">
        <div class="wordmark">
          <span class="wordmark-square"></span>
          <span class="wordmark-name">Ray Dunmore Institute</span>
        </div>
      </div>
      <svg class="cover-art" width="300" height="576" viewBox="0 0 300 576" role="img"
           aria-label="Photo: a man standing on a boulder with arms raised beneath a wide blue sky">
        <defs>
          <linearGradient id="sky-fill" x1="0" y1="0" x2="0" y2="1">
            <stop offset="0" stop-color="#3f74b8"/>
            <stop offset="0.45" stop-color="#8fb0d8"/>
            <stop offset="0.62" stop-color="#d9e3ee"/>
            <stop offset="0.8" stop-color="#9aa6b3"/>
            <stop offset="1" stop-color="#7d746c"/>
          </linearGradient>
        </defs>
        <rect width="300" height="576" fill="var(--navy)"/>
        <path d="M0,40 L60,40 L0,360 Z" fill="url(#sky-fill)"/>
        <path d="M150,28 L272,28 Q296,28 296,52 L296,576 L40,576 Z" fill="url(#sky-fill)"/>
      </svg>
    </section>

    <!-- Join now -->
    <section class="panel join-panel">
      <h2 class="panel-header">Join Now</h2>
      <div class="panel-body">
        <p>Simply click “Join The Bold Circle.” Once you have read the details, press the button below, choose “Begin your path,” a short form will open and you are set.</p>
        <p>During the first six weeks of The Bold Circle, the way you think will change and you will be living a life where your goals become a reality.</p>
        <p>What follows after that will be Life Changing.</p>
        <p>Join today at a special price that is less than one session with a personal coach.</p>
      </div>
      <div class="feature-tiles">
        <div class="feature-tile feature-tile--light">
          <svg width="62" height="50" viewBox="0 0 62 50" aria-hidden="true">
            <rect x="9" y="4" width="44" height="30" rx="2" fill="none" stroke="#fff" stroke-width="3"/>
            <path d="M3,40 H59 L55,46 H7 Z" fill="none" stroke="#fff" stroke-width="3" stroke-linejoin="round"/>
          </svg>
        </div>
        <div class="feature-tile feature-tile--dark">
          <svg width="62" height="50" viewBox="0 0 62 50" aria-hidden="true">
            <rect x="9" y="4" width="44" height="30" rx="2" fill="none" stroke="#fff" stroke-width="3"/>
            <circle cx="31" cy="19" r="8" fill="none" stroke="#fff" stroke-width="2.5"/>
            <path d="M28,15 L35,19 L28,23 Z" fill="#fff"/>
            <path d="M3,40 H59 L55,46 H7 Z" fill="none" stroke="#fff" stroke-width="3" stroke-linejoin="round"/>
          </svg>
        </div>
      </div>
    </section>

    <!-- The Bold Circle -->
    <section class="panel circle-panel">
      <h2 class="panel-header">The Bold Circle</h2>
      <div class="panel-body">
        <p>Life Changing Value for an Unbelievable Price!</p>
        <p>By registering you will:</p>
        <p>1) Become part of The Bold Circle (click “The Bold Circle” tab to learn more). What we have planned for you in 2013 is simply amazing. The community you will be a part of will inspire you to reach further than you thought possible, as we provide you with the framework to meet and exceed your chosen goals. Each week you will receive a Morning Brief, Dr. Dunmore’s personal video explanation of the meaning behind the brief and truly remarkable video commentary from our expert partners. Our partners will blow you away each week with their inspirational approach to providing you with the essential tools for success!</p>
        <p>2) Be able to download Dr. Ray Dunmore’s 52 Morning Briefs (1st edition) immediately via the link provided in your confirmation. These Briefs have been developed by Dr. Dunmore over the past 25 years and have helped many executives, business leaders and business owners build extremely successful companies and enjoy lives that were more meaningful than they ever imagined. The 52 Briefs are for those individuals who are ready to begin the process of working with coaches and mentors while learning how to set goals, network with successful individuals who are on the same path but, for whatever reason, do not have the time and/or the resources to hire a personal coach.</p>
        <p>The impact will be incredible; the results will be Life Changing.</p>
      </div>
      <div class="wordmark">
        <span class="wordmark-square"></span>
        <span class="wordmark-name">Ray Dunmore Institute</span>
      </div>
    </section>
  </main>
</body>
</html>
```